Startup Consultancy - Brochure Design

This needs to be a digital and potential hardcopy of a glossy brochure, designed to really catch the eye of prospective clients and draw them in. I am looking for something alternative from the "usual", but equally in keeping with the IT industry that the business operate in. The business specifically focuses on Print & Document Software and Technology solutions, and this should be considered in the design.

Target Market(s)

SMB and Corporate End Users, + Technology Resellers

Industry/Entity Type

Information Technology

Other font styles liked:
• Avenir

Colors
9d9d9d
848484
c3c3c3
e8e8e8
ffffff
eaeaea
0255a3
3176b5
85acd3

Requirements
Must have
• Company logo displayed on the front, plus any other relevant placements in pages
• Must follow the colour/style in some way of the website (www.brevantadvisory.co.uk)
Nice to have
• Some kind of infographical style in the brochure would be good, perhaps around the service listings

```html
<!DOCTYPE html>
<html lang="en">
<head>
<meta charset="utf-8">
<title>Brevant Advisory – Brochure Inside Spread</title>
<link rel="stylesheet" href="https://fonts.googleapis.com/css2?family=Nunito+Sans:wght@300;400;600;700;800&display=swap">
<style>
  :root {
    --blue: #2f6db2;
    --blue-heading: #2560a8;
    --green: #4fc796;
    --green-light: #6fd6b1;
    --green-text: #3dbf8c;
    --ink: #4a4a4a;
    --paper: #ffffff;
    --backdrop: #e8e8e8;
  }
  * { box-sizing: border-box; margin: 0; padding: 0; }
  html, body { width: 1200px; height: 1200px; overflow: hidden; }
  body {
    background: var(--backdrop);
    font-family: "Nunito Sans", "Avenir", sans-serif;
    display: flex; align-items: center; justify-content: center;
  }
  .spread {
    width: 1140px; height: 806px;
    display: grid; grid-template-columns: repeat(3, 1fr);
    background: var(--paper);
    box-shadow: 0 10px 30px rgba(0,0,0,.12);
  }
  .panel { display: flex; flex-direction: column; position: relative; }
  .panel + .panel { border-left: 1px solid #eeeeee; }
  .block { padding: 0 34px; }
  .block p, .service-list li {
    font-size: 13px; line-height: 1.55; font-weight: 300; color: var(--ink);
  }
  .block p em { font-style: italic; }
  .title {
    font-weight: 800; text-transform: uppercase; letter-spacing: .5px;
    color: var(--blue-heading); font-size: 30px; line-height: 1.05;
  }
  .subtitle { font-weight: 700; color: var(--green-text); font-size: 17px; margin: 2px 0 12px; }
  .band { color: #fff; display: flex; flex-direction: column; justify-content: center; }
  .band p { color: #fff; font-weight: 400; }
  .band--green { background: var(--green); }
  .band--light { background: var(--green-light); }
  .band h3 { font-size: 18px; font-weight: 700; margin-bottom: 8px; }

  /* About */
  .about .intro { padding-top: 78px; height: 372px; }
  .about .band { height: 188px; }
  .about .closing { padding-top: 24px; }
  .about .closing p + p { margin-top: 2px; }

  /* Why */
  .why .intro { padding-top: 44px; height: 300px; }
  .why .band { height: 196px; }
  .why .closing { padding-top: 40px; }

  /* Services */
  .services { background: var(--blue); color: #fff; padding: 36px 40px 0 38px; }
  .services .title { color: var(--green-light); font-size: 30px; }
  .services .subtitle { color: #fff; font-size: 17px; margin-bottom: 12px; }
  .service-list { list-style: none; }
  .service-list li { color: #fff; font-weight: 300; padding-left: 12px; position: relative; margin-bottom: 2px; }
  .service-list li::before { content: "•"; position: absolute; left: 0; }
  .service-list strong { font-weight: 700; }
</style>
</head>
<body>
  <main class="spread">
    <section class="panel about">
      <div class="block intro">
        <h2 class="title">About Us</h2>
        <p class="subtitle">Taking a different path</p>
        <p>We provide services to End User organisations of various sizes, shapes and styles, ranging from SMB through to Enterprise business and even Government, across a range of vertical markets, helping to create forward thinking, future proofed strategic design for Print &amp; Document Workflow solutions – critically however as an entirely independent approach, without any affiliations to manufacturers, software houses or resellers.</p>
      </div>
      <div class="block band band--green">
        <p>Our expertise, experience and services also support Channel Partners, OEM's and Distributors, providing guidance and design services for Print &amp; Document Workflow strategies, promoting a customer led focus, efficiency and our own core values of honesty and reliability.</p>
      </div>
      <div class="block closing">
        <p>As a group of very experienced, highly skilled and senior members of the IT/Print/Document Solutions industry, we grew tired of the lack of true, un-biased and trusted advice and support within the industry that both Channel Partners and End Users alike would often receive.</p>
        <p><em>We don't sell hardware. We don't even sell software.</em></p>
        <p>We remain independent of any manufacturers and are not affiliated to any partner or dealer. What we do provide however is trusted, valuable consultancy, design and advice.</p>
      </div>
    </section>

    <section class="panel why">
      <div class="block intro">
        <h2 class="title">Why Choose Us?</h2>
        <p class="subtitle">An alternative and innovative approach</p>
        <p>We take pride, satisfaction and enjoyment from providing clients with clear, non-bias advice. Our determination to stand alone in the industry without commercial affiliations or ties to ANY particular manufacturer, channel partner or software developers sets us apart from the rest. Our consultancy services also ensure you are aware and prepared for potential pitfalls, complexities and challenges associated with the world of Print &amp; Document solutions.</p>
      </div>
      <div class="block band band--light">
        <h3>How do we do that?</h3>
        <p>Honest and open advice, transparency in our approach and the integrity to ensure we inform our clients if we cannot provide services that are either suitable or to the high standards expected by you or us – if we can't help we will tell you so openly, no fuss, no over promising.</p>
      </div>
      <div class="block closing">
        <p>We also maintain memberships with key industry analysts such as Corvex Insight, Halden Research and more, along with having representation on European Advisory boards with a view to positively contributing to the imaging and printing industry standards. It is our aim to be the most trusted consultancy in our industry, but to do this we have to earn it.</p>
      </div>
    </section>

    <section class="panel services">
      <h2 class="title">Strategy Design<br>Services</h2>
      <p class="subtitle">A roadmap for your future</p>
      <ul class="service-list">
        <li><strong>Stakeholder Interviews &amp; Feedback</strong> – a key element right at the beginning of the process. It is important for us to understand your organisation in detail, its specific areas of business, target markets, competitors and much more.</li>
        <li><strong>Objective &amp; Goal Mapping</strong> – where does your organisation need to get to with any new strategic design, what are the risk factors, and what are the key priorities.</li>
        <li><strong>Departmental/Process Review</strong> – what is done where in the current organisation structure, why and how.</li>
        <li><strong>Gap Analysis</strong> – understanding the gaps and areas to address between the current state and the short/mid-term and long term objectives and goals.</li>
        <li><strong>Strategic Design Proposal</strong> – based on all findings the new strategic design proposal can be created. This must then be agreed and signed off by all relevant stakeholders.</li>
        <li><strong>Final Design &amp; Project Plan</strong> – the final critical element is understanding how and more importantly when all elements of the new strategy can be implemented.</li>
      </ul>
    </section>
  </main>
</body>
</html>
```